Torvel Business Cards

Business card design. dont mind if new logo is suggested.
it would be for a security company.
our clients would be bigger security companies around Australia.
have a logo done but can be replaced. see attaached. like the colors.
Need company name, person name, designation, phone and email on front.
At back company logo and name. website saddress and 2 x license numbers
would like to have 2 different background color for both sidde

Industry/Entity Type

Security

Contact Information for Business Card

round corners, front should be light in color. need logo at back with webaddress and 2 x license numners

Font styles to use
Sans Serif

Colors
f37122
faa54b
f8ba93
0255a3
0592cd
85cae6
b3d448
9bcb3c
ffffff

Requirements
Must have
• see description
Nice to have
• see description
Should not have
• should not be difficult to read or hardd to find information on card.. lets say easy on eyes yet catchy

```html
<!DOCTYPE html>
<html lang="en">
<head>
<meta charset="utf-8">
<title>Torvel Security Group – Business Cards</title>
<link rel="stylesheet" href="https://fonts.googleapis.com/css2?family=Libre+Baskerville&family=Open+Sans:wght@400;600;700&display=swap">
<style>
  :root {
    --stage: #1b1b1b;
    --navy: #1f2f5f;
    --cyan: #0aa6c9;
    --white: #ffffff;
    --ink: #1f2f5f;
    --serif: "Libre Baskerville", Georgia, serif;
    --sans: "Open Sans", Arial, sans-serif;
  }
  * { box-sizing: border-box; margin: 0; padding: 0; }
  html, body { width: 1200px; height: 741px; overflow: hidden; }
  body { background: var(--stage); position: relative; font-family: var(--sans); }

  .card {
    position: absolute;
    top: 229px;
    width: 495px;
    height: 282px;
    border-radius: 12px;
    overflow: hidden;
  }
  .card--front { left: 100px; background: var(--white); color: var(--ink); }
  .card--back  { left: 606px; background: var(--navy); color: var(--white); }

  .dot-field { position: absolute; top: 0; height: 100%; width: 260px; }
  .card--front .dot-field {
    right: 0;
    background:
      radial-gradient(ellipse 150px 160px at 100% 62%, rgba(31,47,95,0.35) 0%, rgba(31,47,95,0) 100%),
      radial-gradient(ellipse 230px 200px at 100% 50%, rgba(10,166,201,0.75) 0%, rgba(10,166,201,0.4) 45%, rgba(10,166,201,0) 100%);
  }
  .card--back .dot-field {
    left: 0;
    background:
      radial-gradient(ellipse 150px 170px at 0% 45%, rgba(10,166,201,0.35) 0%, rgba(10,166,201,0) 100%),
      radial-gradient(ellipse 230px 200px at 0% 50%, rgba(255,255,255,0.55) 0%, rgba(255,255,255,0.25) 45%, rgba(255,255,255,0) 100%);
  }

  .brand-mark {
    position: absolute;
    width: 40px; height: 40px;
    border-radius: 50%;
    background: var(--cyan);
  }
  .card--front .brand-mark { left: 128px; top: 46px; }
  .card--back .brand-mark  { left: 301px; top: 46px; }

  .brand-name {
    position: absolute;
    font-family: var(--serif);
    font-size: 16.5px;
    white-space: nowrap;
  }
  .card--front .brand-name { left: 24px; top: 112px; color: var(--ink); }
  .card--back .brand-name  { left: 321px; top: 114px; transform: translateX(-50%); color: var(--white); }

  .person { position: absolute; left: 24px; top: 179px; }
  .person__name { font-weight: 700; font-size: 17px; line-height: 20px; color: var(--ink); letter-spacing: 0.3px; }
  .person__role { font-size: 13px; line-height: 15px; color: var(--cyan); }

  .contact { position: absolute; left: 24px; top: 226px; list-style: none; font-size: 13px; line-height: 16px; }
  .contact__item { display: flex; align-items: center; gap: 5px; }
  .contact__icon { width: 14px; height: 14px; flex: none; }

  .back-info { position: absolute; left: 321px; transform: translateX(-50%); text-align: center; white-space: nowrap; }
  .licenses { top: 185px; font-size: 13px; line-height: 17px; }
  .website { top: 236px; font-size: 13px; font-weight: 600; letter-spacing: 0.6px; }
</style>
</head>
<body>
  <section class="card card--front" aria-label="Front of card">
    <div class="dot-field" role="img" aria-label="Decorative field of cyan and navy circles along the right edge"></div>
    <span class="brand-mark" aria-hidden="true"></span>
    <p class="brand-name">TORVEL SECURITY GROUP</p>
    <div class="person">
      <p class="person__name">LENA HART</p>
      <p class="person__role">Director</p>
    </div>
    <ul class="contact">
      <li class="contact__item">
        <svg class="contact__icon" viewBox="0 0 14 14" aria-hidden="true">
          <rect width="14" height="14" rx="2" fill="var(--cyan)"/>
          <path d="M3 5.5c0-1 1.8-2 4-2s4 1 4 2v0.8H9V5.2H5v1.1H3z M4.5 7h5l1 3.5h-7z" fill="#fff"/>
        </svg>
        <span>555.204.7318</span>
      </li>
      <li class="contact__item">
        <svg class="contact__icon" viewBox="0 0 14 14" aria-hidden="true">
          <rect width="14" height="14" rx="2" fill="var(--cyan)"/>
          <rect x="2.5" y="4" width="9" height="6.5" fill="#fff"/>
          <path d="M2.5 4l4.5 3.6L11.5 4" fill="none" stroke="var(--cyan)" stroke-width="1"/>
        </svg>
        <span>lena@torvelgroup.com</span>
      </li>
    </ul>
  </section>

  <section class="card card--back" aria-label="Back of card">
    <div class="dot-field" role="img" aria-label="Decorative field of white and cyan circles along the left edge"></div>
    <span class="brand-mark" aria-hidden="true"></span>
    <p class="brand-name">TORVEL SECURITY GROUP</p>
    <p class="back-info licenses">License number 123456<br>License number 123456</p>
    <p class="back-info website">www.torvelgroup.com</p>
  </section>
</body>
</html>
```